8' X 8" convention booth design

I am requesting a design for a convention booth. This design must be created in Adobe Illustrator.
I sell insurance programs to the members of associations. My prospects that will see this booth are association professionals looking to select a provider of insurance benefits for their memberships. I would like my prospects to look at my booth, see our logo, understand what we do, and then show some icons highlighting the insurance products that we have available. Please feel free to add any pictures or anything you might find to make the booth more appealing, but are not necessary. I have attached a photo of a sample of the booth construction below for your review.
The booth is 8’ X 8’ in the front and will have two 1’ side panels on each side. The dimensions of the front graphics are 87.75” W X 87.75” H. Each of the two side panel is 12 W X 87.75” H. The total width of the design is 111.75”. The graphic should be designed to include the 12’ wrap around on each side.
I have attached two of our logos below. The attached Nesterra logo with the words "Affinity and Association Services" is the logo for the front of the booth. The plain Nesterra logo is for the top of the side panels.
For side panels, please put the Nesterra logo (with only the Nesterra letters) at the top and the words "Association Insurance" underneath the Nesterra logo. The Association Insurance letters should be vertical.
For the front of the booth, I would like to have the Nesterra logo somewhere prominent in your design. I do not want it too big, but would like people to notice my company logo and description line. Also on the front of the booth, please include the following information that describes my company:
Full Portfolio of Insurance Products
Brokerage with A-Rated insurance companies
Full-Service Administrator
State-of-the-Art Technologies
Multi-Channel Marketing
The header for this section of five bullets above can be Member Insurance Program Management.
Lastly, I have attached 14 other icons that represent the insurance products I am offering. Please place them in a grid, or some other creative way, and include the word I have used to name each icon below each icon. For example, please type the word Life under the Life icon in the design. If you are looking for a header for this section, it can be Insurance Products Thank you very much for your interest.
Association Executive Directors looking to offer valuable member benefits to their association membership.

```html
<!DOCTYPE html>
<html lang="en">
<head>
<meta charset="utf-8">
<title>Nesterra Association Insurance – Booth Graphic</title>
<link rel="stylesheet" href="https://fonts.googleapis.com/css2?family=Lato:ital,wght@0,400;0,700;0,900;1,400&display=swap">
<style>
  :root {
    --olive: #a3a83a;
    --olive-soft: #e6e9cf;
    --grey-soft: #d8dadc;
    --navy: #27344a;
    --ink: #2f3133;
    --muted: #55585c;
    --white: #ffffff;
  }
  * { margin: 0; padding: 0; box-sizing: border-box; }
  html, body { width: 1200px; height: 1200px; overflow: hidden; background: var(--white); }
  body { font-family: "Lato", Arial, sans-serif; color: var(--ink); }

  .booth { position: relative; width: 1200px; height: 1200px; overflow: hidden; background: var(--white); }
  .backdrop { position: absolute; inset: 0; }

  .side-panel { position: absolute; top: 0; width: 150px; height: 1200px; background: var(--olive); }
  .side-panel--left { left: 0; }
  .side-panel--right { right: 0; }

  .side-brand, .side-title, .side-rule {
    position: absolute; color: var(--white); white-space: nowrap; line-height: 1;
  }
  .side-brand { font-weight: 900; font-size: 34px; letter-spacing: 1px; }
  .side-title { font-weight: 400; font-size: 52px; letter-spacing: 0.5px; }
  .side-rule { font-weight: 400; font-size: 30px; letter-spacing: 1px; opacity: .75; }

  .side-panel--left .side-brand { left: 80px; top: 222px; transform: translate(-50%, -50%) rotate(90deg); }
  .side-panel--left .side-rule  { left: 80px; top: 318px; transform: translate(-50%, -50%) rotate(90deg); }
  .side-panel--left .side-title { left: 80px; top: 685px; transform: translate(-50%, -50%) rotate(90deg); }

  .side-panel--right .side-brand { left: 76px; top: 978px; transform: translate(-50%, -50%) rotate(-90deg); }
  .side-panel--right .side-rule  { left: 76px; top: 885px; transform: translate(-50%, -50%) rotate(-90deg); }
  .side-panel--right .side-title { left: 78px; top: 513px; transform: translate(-50%, -50%) rotate(-90deg); }

  .brand { position: absolute; left: 245px; top: 140px; display: flex; align-items: center; }
  .brand-name { font-weight: 900; font-size: 60px; color: var(--olive); letter-spacing: 0.5px; line-height: 1; }
  .brand-rule { margin-left: 18px; width: 26px; height: 46px; flex: none; }
  .brand-tagline { margin-left: 14px; font-style: italic; font-size: 19px; letter-spacing: 2.4px; color: var(--muted); white-space: nowrap; }

  .benefits { position: absolute; left: 243px; top: 286px; list-style: none; }
  .benefits li { display: flex; align-items: center; height: 40px; font-size: 31px; font-weight: 700; color: var(--ink); }
  .benefits svg { width: 26px; height: 26px; margin-right: 15px; flex: none; }

  .products-frame { position: absolute; inset: 0; }
  .products-title {
    position: absolute; left: 599px; top: 604px; transform: translateX(-50%);
    font-size: 29px; font-weight: 900; color: var(--olive); letter-spacing: .3px; white-space: nowrap;
  }

  .product { position: absolute; width: 150px; text-align: center; transform: translateX(-50%); }
  .product-icon {
    width: 114px; height: 114px; margin: 0 auto; border-radius: 50%;
    border: 3px solid var(--olive); background: var(--olive-soft);
  }
  .product-label { margin-top: 12px; font-size: 19px; font-weight: 700; color: var(--ink); white-space: nowrap; }
</style>
</head>
<body>
<main class="booth">

  <svg class="backdrop" width="1200" height="1200" viewBox="0 0 1200 1200" aria-hidden="true">
    <polygon points="870,0 1050,0 1050,175" fill="var(--grey-soft)"/>
    <polygon points="880,55 1050,205 1050,320 880,170" fill="var(--olive-soft)" opacity=".8"/>
    <polygon points="935,60 1050,160 1050,200 935,100" fill="var(--grey-soft)" opacity=".7"/>
    <polygon points="150,470 330,620 330,1200 150,1200" fill="var(--grey-soft)" opacity=".7"/>
    <polygon points="150,760 520,1060 800,1200 150,1200" fill="var(--grey-soft)" opacity=".55"/>
    <polygon points="150,980 420,1200 150,1200" fill="var(--olive-soft)" opacity=".9"/>
    <polygon points="230,760 330,840 330,1010 230,930" fill="var(--olive-soft)" opacity=".8"/>
  </svg>

  <aside class="side-panel side-panel--left">
    <span class="side-brand">NESTERRA</span>
    <span class="side-rule">///</span>
    <span class="side-title">ASSOCIATION INSURANCE</span>
  </aside>

  <aside class="side-panel side-panel--right">
    <span class="side-brand">NESTERRA</span>
    <span class="side-rule">///</span>
    <span class="side-title">ASSOCIATION INSURANCE</span>
  </aside>

  <header class="brand">
    <span class="brand-name">Nesterra</span>
    <svg class="brand-rule" viewBox="0 0 26 46" aria-hidden="true">
      <line x1="6" y1="44" x2="10" y2="2" stroke="var(--muted)" stroke-width="1.6"/>
      <line x1="12" y1="44" x2="16" y2="2" stroke="var(--muted)" stroke-width="1.6"/>
      <line x1="18" y1="44" x2="22" y2="2" stroke="var(--muted)" stroke-width="1.6"/>
    </svg>
    <span class="brand-tagline">AFFINITY &amp; ASSOCIATION SERVICES</span>
  </header>

  <ul class="benefits">
    <li><svg viewBox="0 0 26 26"><circle cx="12" cy="14" r="10" fill="none" stroke="var(--olive)" stroke-width="2.4"/><path d="M7 14l4 4 11-12" fill="none" stroke="var(--navy)" stroke-width="2.6" stroke-linecap="round"/></svg>Full Portfolio of Insurance Products</li>
    <li><svg viewBox="0 0 26 26"><circle cx="12" cy="14" r="10" fill="none" stroke="var(--olive)" stroke-width="2.4"/><path d="M7 14l4 4 11-12" fill="none" stroke="var(--navy)" stroke-width="2.6" stroke-linecap="round"/></svg>Brokerage with A-Rated insurance companies</li>
    <li><svg viewBox="0 0 26 26"><circle cx="12" cy="14" r="10" fill="none" stroke="var(--olive)" stroke-width="2.4"/><path d="M7 14l4 4 11-12" fill="none" stroke="var(--navy)" stroke-width="2.6" stroke-linecap="round"/></svg>Full-Service Administrator</li>
    <li><svg viewBox="0 0 26 26"><circle cx="12" cy="14" r="10" fill="none" stroke="var(--olive)" stroke-width="2.4"/><path d="M7 14l4 4 11-12" fill="none" stroke="var(--navy)" stroke-width="2.6" stroke-linecap="round"/></svg>State-of-the-Art Technologies</li>
    <li><svg viewBox="0 0 26 26"><circle cx="12" cy="14" r="10" fill="none" stroke="var(--olive)" stroke-width="2.4"/><path d="M7 14l4 4 11-12" fill="none" stroke="var(--navy)" stroke-width="2.6" stroke-linecap="round"/></svg>Multi-Channel Marketing</li>
  </ul>

  <svg class="products-frame" width="1200" height="1200" viewBox="0 0 1200 1200" aria-hidden="true">
    <polyline points="405,622 243,622 243,1055 330,1055" fill="none" stroke="var(--navy)" stroke-width="5"/>
    <polyline points="796,622 958,622 958,1055 870,1055" fill="none" stroke="var(--navy)" stroke-width="5"/>
  </svg>
  <h2 class="products-title">INSURANCE PRODUCTS</h2>

  <section class="products">
    <div class="product" style="left:337px;top:658px"><div class="product-icon" role="img" aria-label="Travel icon: airplane"></div><p class="product-label">Travel</p></div>
    <div class="product" style="left:468px;top:658px"><div class="product-icon" role="img" aria-label="Vision icon: eye on shield"></div><p class="product-label">Vision</p></div>
    <div class="product" style="left:599px;top:658px"><div class="product-icon" role="img" aria-label="Accident icon: figure falling on stairs"></div><p class="product-label">Accident</p></div>
    <div class="product" style="left:730px;top:658px"><div class="product-icon" role="img" aria-label="Auto icon: car with protective shield"></div><p class="product-label">Auto</p></div>
    <div class="product" style="left:861px;top:658px"><div class="product-icon" role="img" aria-label="Long-term care icon: elderly figure with walker"></div><p class="product-label">Long-Term Care</p></div>

    <div class="product" style="left:337px;top:824px"><div class="product-icon" role="img" aria-label="Rx cards icon: prescription scroll and pill bottle"></div><p class="product-label">Rx Cards</p></div>
    <div class="product" style="left:468px;top:824px"><div class="product-icon" role="img" aria-label="Business icon: figure under umbrella with dollar sign"></div><p class="product-label">Business</p></div>
    <div class="product" style="left:599px;top:824px"><div class="product-icon" role="img" aria-label="Dental icon: tooth on shield"></div><p class="product-label">Dental</p></div>
    <div class="product" style="left:730px;top:824px"><div class="product-icon" role="img" aria-label="Family health icon: family under umbrella"></div><p class="product-label">Family Health</p></div>
    <div class="product" style="left:861px;top:824px"><div class="product-icon" role="img" aria-label="Financial icon: money bag under umbrella"></div><p class="product-label">Financial</p></div>

    <div class="product" style="left:403px;top:991px"><div class="product-icon" role="img" aria-label="Health icon: medical shield and clipboard"></div><p class="product-label">Health</p></div>
    <div class="product" style="left:534px;top:991px"><div class="product-icon" role="img" aria-label="Life icon: group of people"></div><p class="product-label">Life</p></div>
    <div class="product" style="left:665px;top:991px"><div class="product-icon" role="img" aria-label="Liability icon: figure holding scales"></div><p class="product-label">Liability</p></div>
    <div class="product" style="left:796px;top:991px"><div class="product-icon" role="img" aria-label="Home icon: house held in hands"></div><p class="product-label">Home</p></div>
  </section>

</main>
</body>
</html>
```